TK Drafting

Simple Design - Logo is done (from this site). Logo on one side - Back Side an image or outline of a house blue print - My name, phone, email, website url. Prefer the traditional Architectural style of letters -

Target Market(s)

Customers who need a floor plan redesigned for renovations or realtors who want a floor plan for marketing their listings

Industry/Entity Type

Architecture

Contact Information for Business Card

Colby Faust - Name
415-362-8840 - Phone
tkdraftingco@mailpost.example
www.tkdraftingco.example

Font styles to use
Other font styles liked:
• Architecture writing -

Colors
0555a3
3276b5
85acd3

Requirements
Must have
• Logo that is attached. I like an indigo blue color for the background or a royal blue - gray logo OR - white and clean with the logo on one side and the same color gray lettering on the other side
Nice to have
• some sort of image that shows a residential blue print. It may not be possible on this small of a card though.
Should not have
• Nothing cartoonish.

```html
<!DOCTYPE html>
<html lang="en">
<head>
<meta charset="utf-8">
<title>TK Drafting — Business Card</title>
<link href="https://fonts.googleapis.com/css2?family=Roboto:wght@400;500;700&display=swap" rel="stylesheet">
<style>
  :root {
    --backdrop: #2b2b2b;
    --backdrop-edge: #1c1c1c;
    --card-blue: #0b3a80;
    --card-blue-deep: #082d66;
    --mark-gray: #c3cde0;
    --text-gray: #d4dae6;
    --text-soft: #b4bfd4;
  }
  * { box-sizing: border-box; margin: 0; padding: 0; }
  html, body { width: 1200px; height: 900px; overflow: hidden; }
  body {
    background: radial-gradient(ellipse at center, var(--backdrop) 0%, var(--backdrop-edge) 100%);
    font-family: "Roboto", Arial, sans-serif;
    display: flex;
    align-items: center;
    justify-content: center;
    gap: 56px;
  }
  .card {
    width: 525px;
    height: 300px;
    position: relative;
    background: linear-gradient(150deg, var(--card-blue) 0%, var(--card-blue-deep) 100%);
    border-radius: 3px;
    box-shadow: 0 14px 30px rgba(0,0,0,0.45);
  }
  .brand {
    display: flex;
    align-items: center;
    gap: 12px;
    color: var(--mark-gray);
    font-weight: 500;
    letter-spacing: 0.06em;
    white-space: nowrap;
  }
  .brand-square {
    background: var(--mark-gray);
    border-radius: 2px;
  }
  .card-front { display: flex; align-items: center; justify-content: center; }
  .card-front .brand { font-size: 40px; }
  .card-front .brand-square { width: 34px; height: 34px; }

  .contact {
    position: absolute;
    left: 40px;
    top: 42px;
    color: var(--text-gray);
  }
  .contact-name { font-size: 17px; font-weight: 700; letter-spacing: 0.03em; text-transform: uppercase; }
  .contact-role { font-size: 13px; color: var(--text-soft); margin: 2px 0 14px; }
  .contact-line { display: flex; align-items: center; gap: 8px; font-size: 14px; line-height: 22px; white-space: nowrap; }
  .contact-line svg { width: 13px; height: 13px; flex: none; }
  .card-back .brand {
    position: absolute;
    right: 40px;
    bottom: 52px;
    font-size: 26px;
  }
  .card-back .brand-square { width: 22px; height: 22px; }
</style>
</head>
<body>
  <section class="card card-back">
    <div class="contact">
      <p class="contact-name">Colby Faust</p>
      <p class="contact-role">Director</p>
      <p class="contact-line">
        <svg viewBox="0 0 16 16" fill="var(--text-gray)"><path d="M3.5 1.5l2.5 0 1 3.5-1.6 1.2a9 9 0 0 0 4.4 4.4L11 9l3.5 1v2.5c0 .8-.7 1.5-1.5 1.5A11.5 11.5 0 0 1 2 3c0-.8.7-1.5 1.5-1.5z"/></svg>
        415-362-8840
      </p>
      <p class="contact-line">
        <svg viewBox="0 0 16 16" fill="var(--text-gray)"><rect x="1" y="3" width="14" height="10" rx="1"/><path d="M1.5 3.5L8 9l6.5-5.5" stroke="var(--card-blue)" stroke-width="1.4" fill="none"/></svg>
        tkdraftingco@mailpost.example
      </p>
      <p class="contact-line">
        <svg viewBox="0 0 16 16" fill="none" stroke="var(--text-gray)" stroke-width="1.3"><circle cx="8" cy="8" r="6.5"/><ellipse cx="8" cy="8" rx="3" ry="6.5"/><path d="M1.5 8h13"/></svg>
        www.tkdraftingco.example
      </p>
    </div>
    <div class="brand">
      <span class="brand-square"></span>
      <span class="brand-name">TK Drafting</span>
    </div>
  </section>

  <section class="card card-front">
    <div class="brand">
      <span class="brand-square"></span>
      <span class="brand-name">TK Drafting</span>
    </div>
  </section>
</body>
</html>
```